Podiatry clinic requires a modern revamp and editing of existing website.

I would like a fresh new look and updated information for my current business website. An easy to navigate site with prominent address and phone number for call to action. We are a podiatry clinic that focuses on general and sports podiatry.
I would like 4 pages; including Home page, About Us, Services & Contact.
www.brambleridgefootcare.com

Target Market(s)

Active working professionals.

Industry/Entity Type

Medical

Coding

Coded - Design and coding required

Number of Pages Required

4 page

Font styles to use
Sans Serif

Colors
6b449b

Requirements
Must have
• A modern look with logo and active images; clean and uncluttered. Visible phone number and address for call to action.
• 4 pages - Home, About Us, Services, Contact.
• Home page - update address & service logos.
• About Us - update of personal information.
• Services - Revamp of existing page.
• Contact page to include Google map, email & phone number.
Nice to have
• Ability to add content easily; eg. a blog or adding video onto Home page.
• Link to Facebook page.

```html
<!DOCTYPE html>
<html lang="en">
<head>
<meta charset="utf-8">
<title>Bramble Ridge Foot Care</title>
<link href="https://fonts.googleapis.com/css2?family=Raleway:wght@500;600;700&family=Lato:wght@400;700&display=swap" rel="stylesheet">
<style>
:root{
  --purple:#6b449b;
  --purple-deep:#46309a;
  --lilac:#9b86c2;
  --yellow:#f8c21b;
  --orange:#f39a2b;
  --cta:#ff3d12;
  --grey:#5f5f5f;
  --grey-bar:#6b6b6b;
  --ink:#222;
  --green:#7ab317;
  --red:#e8120f;
  --white:#fff;
}
*{box-sizing:border-box;margin:0;padding:0}
html,body{width:1200px;height:2473px;overflow:hidden}
body{position:relative;background:var(--white);font-family:"Lato",Arial,sans-serif;color:var(--ink)}
.abs{position:absolute}
.header{left:0;top:0;width:1200px;height:87px;background:var(--lilac)}
.brand{display:flex;align-items:center;gap:8px;font-family:"Raleway",sans-serif;font-weight:700;color:var(--orange);font-size:17px;line-height:18px}
.brand-dot{width:22px;height:22px;border-radius:50%;background:var(--purple-deep);flex:none}
.nav{left:482px;top:50px;display:flex;gap:0;font-family:"Raleway",sans-serif;font-weight:600;font-size:17px;color:var(--white)}
.nav a{color:inherit;text-decoration:none;position:absolute;white-space:nowrap}
.nav .active{color:var(--orange)}
.head-divider{left:875px;top:18px;width:1px;height:50px;background:rgba(255,255,255,.6)}
.head-call{left:902px;top:24px;display:flex;align-items:center;gap:12px;color:var(--white)}
.call-icon{width:32px;height:32px;border:2px solid var(--white);border-radius:50%;display:flex;align-items:center;justify-content:center}
.head-call small{display:block;font-size:15px}
.head-call strong{display:block;font-size:21px;font-weight:400;color:#2b2b2b}
.slider{left:0;top:87px;width:1200px;height:358px;display:flex}
.slide{height:100%}
.slider-arrow{top:292px;width:38px;height:36px;border:1px solid rgba(255,255,255,.7);display:flex;align-items:center;justify-content:center}
.tagline{left:0;top:448px;width:1200px;height:50px;background:var(--purple);color:var(--white);font-family:"Raleway",sans-serif;font-size:25px;font-weight:500;text-align:center;line-height:50px}
.tagline b{font-weight:700}
.service{top:522px;height:290px;overflow:hidden}
.service h3{height:41px;background:var(--yellow);color:var(--purple-deep);font-family:"Raleway",sans-serif;font-weight:700;font-size:20px;text-align:center;line-height:41px}
.service-photo{height:249px}
.service p{position:absolute;left:0;bottom:0;width:100%;height:85px;background:rgba(107,68,155,.82);color:var(--white);font-size:13.5px;line-height:24px;text-align:center;padding:6px 14px}
.welcome-shade{left:600px;top:845px;width:600px;height:70px;background:linear-gradient(180deg,rgba(0,0,0,.12),rgba(0,0,0,0))}
.section-title{font-family:"Raleway",sans-serif;font-weight:500;text-align:center;width:1200px;left:0}
.divider{height:12px}
.welcome-text{left:148px;top:958px;width:904px;text-align:center;font-family:Arial,sans-serif;font-size:14.5px;line-height:27.5px;color:#333}
.appoint{left:0;top:1076px;width:1200px;text-align:center;font-family:Arial,sans-serif;font-weight:700;font-size:14.5px;line-height:24px;color:#111}
.accred{left:0;top:1157px;width:1200px;height:305px;background:var(--grey)}
.badge{top:1289px;height:77px;background:var(--white)}
.badge-inner{position:absolute;left:20px;top:18px;right:20px;bottom:18px;border-radius:6px}
.blogzone{left:0;top:1462px;width:1200px;height:494px;background:linear-gradient(100deg,#dcdcdf 0%,#f1f1f1 35%,#ebe8ee 60%,#f4eff5 100%)}
.col-title{font-family:Arial,sans-serif;font-size:33px;color:#1b1b1b}
.post{left:125px;width:440px;height:66px}
.post-date{position:absolute;left:0;top:0;width:70px;height:66px;color:var(--white);text-align:center;font-family:Arial,sans-serif}
.post-date b{display:block;font-size:34px;font-weight:400;line-height:42px}
.post-date span{display:block;font-size:16px;line-height:18px}
.post h4{position:absolute;left:94px;top:2px;width:310px;font-family:Arial,sans-serif;font-size:17px;font-weight:400;color:#333;border-bottom:1px solid #999;padding-bottom:3px}
.post p{position:absolute;left:94px;top:28px;width:320px;font-family:Arial,sans-serif;font-size:11.5px;line-height:17px;color:#444}
.post i{display:inline-block;width:11px;height:11px;background:var(--orange);margin-left:12px;vertical-align:middle}
.video-frame{left:692px;top:1623px;width:376px;height:261px;background:var(--yellow);box-shadow:0 4px 8px rgba(0,0,0,.25)}
.video-screen{position:absolute;left:23px;top:18px;width:332px;height:200px;background:linear-gradient(135deg,#e9eef2,#c9d3dc 60%,#a9b4c0)}
.video-bar{position:absolute;left:23px;top:218px;width:332px;height:28px;background:#1b1b1b;display:flex;align-items:center;padding:0 10px;gap:10px}
.cta-line{left:127px;font-family:"Raleway",sans-serif;font-size:21px;line-height:30px;color:#555}
.cta-btn{left:766px;top:2019px;width:216px;height:61px;background:var(--cta);border-radius:4px;color:var(--white);text-align:center;font-family:Arial,sans-serif;box-shadow:0 2px 4px rgba(0,0,0,.3)}
.cta-btn small{display:block;font-size:16px;padding-top:6px}
.cta-btn strong{display:block;font-size:24px;font-weight:400;line-height:28px}
.footer{left:0;top:2175px;width:1200px;height:251px;background:var(--lilac);color:#1e1e1e;font-family:"Lato",sans-serif}
.foot-h{font-family:"Raleway",sans-serif;font-weight:600;font-size:18px;color:#2b2b2b}
.foot-links{list-style:none;font-size:13.5px;line-height:25px}
.foot-links li::before{content:"›";margin-right:12px;color:#444}
.foot-sep{width:1px;background:rgba(255,255,255,.35)}
.foot-text{font-size:13.5px;line-height:19px}
.bottom{left:0;top:2426px;width:1200px;height:47px;background:var(--grey-bar);color:#eee;font-size:13.5px;line-height:47px;padding-left:132px}
.social{top:2434px;width:32px;height:32px;border-radius:50%;background:#8a8a8a}
</style>
</head>
<body>

<header class="abs header">
  <div class="abs brand" style="left:140px;top:8px">
    <span class="brand-dot"></span>
    <span>bramble ridge<br>foot<br>care</span>
  </div>
  <svg class="abs" style="left:478px;top:0" width="36" height="10" viewBox="0 0 36 10"><path d="M4 0h28L18 9z" fill="var(--orange)"/></svg>
  <nav class="abs nav">
    <a class="active" style="left:0">Home</a>
    <a style="left:80px">About Us</a>
    <a style="left:186px">Services</a>
    <a style="left:286px">Contact Us</a>
  </nav>
  <div class="abs head-divider"></div>
  <div class="abs head-call">
    <span class="call-icon"><svg width="16" height="16" viewBox="0 0 24 24"><path d="M6.6 10.8a15 15 0 0 0 6.6 6.6l2.2-2.2c.3-.3.7-.4 1-.2 1.1.4 2.3.6 3.6.6.6 0 1 .4 1 1V20c0 .6-.4 1-1 1A17 17 0 0 1 3 4c0-.6.4-1 1-1h3.5c.6 0 1 .4 1 1 0 1.3.2 2.5.6 3.6.1.3 0 .7-.2 1z" fill="#fff"/></svg></span>
    <span><small>Call Us Today</small><strong>1300 482 907</strong></span>
  </div>
</header>

<section class="abs slider">
  <div class="slide" role="img" aria-label="Golfer mid swing on a course" style="width:136px;background:linear-gradient(180deg,#5d7a55,#8fa37a 60%,#c9c9c0)"></div>
  <div class="slide" role="img" aria-label="Woman running on a country road" style="width:240px;background:linear-gradient(180deg,#7d8f5a,#4f5a3c 55%,#8b8d86)"></div>
  <div class="slide" role="img" aria-label="Cyclists racing in a group" style="width:225px;background:linear-gradient(180deg,#8a8a74,#5a5a4c 55%,#9a9a8e)"></div>
  <div class="slide" role="img" aria-label="Dancer leaping in black and white" style="width:276px;background:linear-gradient(180deg,#3a3a3a,#8a8a8a 70%,#d0d0d0)"></div>
  <div class="slide" role="img" aria-label="Footballer kicking a ball on a dirt pitch" style="width:204px;background:linear-gradient(180deg,#b7a48c,#a2533a 70%,#c16a45)"></div>
  <div class="slide" role="img" aria-label="Basketball player jumping to shoot" style="width:119px;background:linear-gradient(180deg,#3a2e2a,#6a4a3a 60%,#a47a58)"></div>
  <div class="abs slider-arrow" style="left:2px;top:205px"><svg width="10" height="16" viewBox="0 0 10 16"><path d="M8 2 2 8l6 6" stroke="#fff" stroke-width="2" fill="none"/></svg></div>
  <div class="abs slider-arrow" style="left:1160px;top:205px"><svg width="10" height="16" viewBox="0 0 10 16"><path d="m2 2 6 6-6 6" stroke="#fff" stroke-width="2" fill="none"/></svg></div>
</section>

<div class="abs tagline"><b>bramble ridge foot care</b> is a podiatry clinic in the heart of melbourne CBD</div>

<article class="abs service" style="left:127px;width:290px">
  <h3>Sports Injuries</h3>
  <div class="service-photo" role="img" aria-label="Hands treating an injured ankle" style="background:linear-gradient(160deg,#e9e2dc,#d9b9a4 55%,#3b3b3b)"></div>
  <p>Lorem ipsum dolor sit amet, consectetuer adipiscing elit, sed diam nonummy nibh euismod tincidunt ut laoreet.</p>
</article>
<article class="abs service" style="left:452px;width:285px">
  <h3>Orthotic Therapy</h3>
  <div class="service-photo" role="img" aria-label="Orthotic insole fitted against a foot" style="background:linear-gradient(160deg,#f2eeea,#d8b8a0 55%,#b89a86)"></div>
  <p>Lorem ipsum dolor sit amet, consectetuer adipiscing elit, sed diam nonummy nibh euismod tincidunt ut laoreet.</p>
</article>
<article class="abs service" style="left:780px;width:286px">
  <h3>Nail Surgery</h3>
  <div class="service-photo" role="img" aria-label="Gloved hands treating a toenail" style="background:linear-gradient(160deg,#dfe6ea,#e6b89a 55%,#d86a3a)"></div>
  <p>Lorem ipsum dolor sit amet, consectetuer adipiscing elit, sed diam nonummy nibh euismod tincidunt ut laoreet.</p>
</article>

<section>
  <div class="abs welcome-shade"></div>
  <svg class="abs" style="left:0;top:845px" width="283" height="210"><path d="M0 0h283L0 210z" fill="var(--yellow)"/></svg>
  <h2 class="abs section-title" style="top:884px;font-size:26px;color:#1b1b1b">Welcome to Bramble Ridge Foot Care</h2>
  <svg class="abs divider" style="left:315px;top:923px" width="545" height="12"><rect x="0" y="4" width="10" height="5" fill="var(--yellow)"/><rect x="18" y="4" width="10" height="5" fill="var(--purple-deep)"/><rect x="40" y="5" width="465" height="3" fill="var(--yellow)"/><rect x="517" y="4" width="10" height="5" fill="var(--purple-deep)"/><rect x="535" y="4" width="10" height="5" fill="var(--yellow)"/></svg>
  <p class="abs welcome-text">Bramble Ridge Foot Care is a Podiatry clinic in the heart of Melbourne CBD. We are located between Harlow &amp; Denby Streets in the Eastgate Business Centre / Linden Hotel Complex. Our podiatrists are fully qualified health professionals who are able to diagnose, treat, manage or help to prevent all medical conditions that affect the feet and lower limb.We provide General Podiatry Treatment and some Specialised Services in relation to various foot conditions, including Sports Injuries, Orthotic Therapy and Nail Surgery.</p>
  <p class="abs appoint">For Appointments or Enquiries please<br>call us on 1300 482 907 &nbsp;or email: &nbsp; info@brambleridgefootcare.com</p>
</section>

<section class="abs accred">
  <svg class="abs" style="left:939px;top:112px" width="261" height="193"><path d="M261 0v193H0z" fill="var(--purple-deep)"/></svg>
  <h2 class="abs section-title" style="top:24px;font-size:34px;color:var(--white)">Our Accreditations</h2>
  <svg class="abs divider" style="left:315px;top:73px" width="545" height="12"><rect x="0" y="4" width="10" height="5" fill="var(--yellow)"/><rect x="18" y="4" width="10" height="5" fill="var(--purple-deep)"/><rect x="40" y="5" width="465" height="3" fill="var(--yellow)"/><rect x="517" y="4" width="10" height="5" fill="var(--purple-deep)"/><rect x="535" y="4" width="10" height="5" fill="var(--yellow)"/></svg>
</section>
<div class="abs badge" style="left:176px;width:203px"><div class="badge-inner" style="background:#dfe3f0"></div></div>
<div class="abs badge" style="left:400px;width:203px"><div class="badge-inner" style="background:#dce6f3"></div></div>
<div class="abs badge" style="left:626px;width:205px"><div class="badge-inner" style="background:#e6e6e6"></div></div>
<div class="abs badge" style="left:850px;width:205px"><div class="badge-inner" style="background:#d7efdc"></div></div>

<section class="abs blogzone" role="img" aria-label="Soft blurred office scene with a laptop and coloured lights">
  <svg class="abs" style="left:0;top:0" width="272" height="202"><path d="M0 0h272L0 202z" fill="var(--yellow)"/></svg>
</section>
<h2 class="abs col-title" style="left:124px;top:1527px">Latest Blog</h2>
<svg class="abs divider" style="left:130px;top:1586px" width="430" height="12"><rect x="0" y="4" width="10" height="5" fill="var(--yellow)"/><rect x="18" y="4" width="10" height="5" fill="var(--purple-deep)"/><rect x="40" y="5" width="390" height="3" fill="var(--yellow)"/></svg>

<div class="abs post" style="top:1618px"><div class="post-date" style="background:var(--green)"><b>03</b><span>Aug</span></div><h4>Lorem ipsum dolor</h4><p>Lorem ipsum dolor sit amet, consectetuer adipiscing elit, sed diam nonummy nibh euismod<i></i></p></div>
<div class="abs post" style="top:1722px"><div class="post-date" style="background:var(--yellow)"><b>01</b><span>Aug</span></div><h4>Lorem ipsum dolor</h4><p>Lorem ipsum dolor sit amet, consectetuer adipiscing elit, sed diam nonummy nibh euismod<i></i></p></div>
<div class="abs post" style="top:1826px"><div class="post-date" style="background:var(--red)"><b>01</b><span>Aug</span></div><h4>Lorem ipsum dolor</h4><p>Lorem ipsum dolor sit amet, consectetuer adipiscing elit, sed diam nonummy nibh euismod<i></i></p></div>

<h2 class="abs col-title" style="left:689px;top:1527px">Our Video</h2>
<svg class="abs divider" style="left:682px;top:1586px" width="384" height="12"><rect x="0" y="4" width="10" height="5" fill="var(--yellow)"/><rect x="18" y="4" width="10" height="5" fill="var(--purple-deep)"/><rect x="40" y="5" width="344" height="3" fill="var(--yellow)"/></svg>

<div class="abs video-frame">
  <div class="video-screen" role="img" aria-label="Video still of a clinic consultation with a handshake"></div>
  <svg class="abs" style="left:169px;top:100px" width="40" height="36"><rect width="40" height="36" rx="8" fill="#111"/><path d="M15 10v16l13-8z" fill="#fff"/></svg>
  <div class="video-bar">
    <svg width="10" height="12"><path d="M0 0v12l10-6z" fill="#ddd"/></svg>
    <svg width="14" height="12"><path d="M0 4h4l5-4v12l-5-4H0z" fill="#ddd"/></svg>
    <svg width="250" height="8"><rect width="250" height="4" y="2" rx="2" fill="#555"/><rect width="110" height="4" y="2" rx="2" fill="#d22"/></svg>
    <svg width="12" height="12"><path d="M0 4V0h4M8 0h4v4M12 8v4H8M4 12H0V8" stroke="#ddd" stroke-width="2" fill="none"/></svg>
  </div>
</div>

<section>
  <svg class="abs" style="left:898px;top:1961px" width="302" height="214"><path d="M302 0v214H0z" fill="var(--purple-deep)"/></svg>
  <p class="abs cta-line" style="top:2012px">We are eligible service providers for all<br>Veterans Gold Card holders</p>
  <p class="abs cta-line" style="top:2089px;color:var(--purple-deep)">Road Injury &amp; Workcover accepted. <span style="color:var(--cta)">On the spot Health insurance</span></p>
  <div class="abs cta-btn"><small>Call Us Today</small><strong>1300 482 907</strong></div>
</section>

<footer class="abs footer">
  <h4 class="abs foot-h" style="left:135px;top:26px">Quick Links</h4>
  <ul class="abs foot-links" style="left:135px;top:70px">
    <li>Consulting</li><li>Inspections</li><li>Training</li><li>General Contracing</li><li>Clients</li><li>Contact Us</li>
  </ul>
  <div class="abs foot-sep" style="left:315px;top:60px;height:170px"></div>
  <h4 class="abs foot-h" style="left:358px;top:26px">Contact Details</h4>
  <svg class="abs" style="left:360px;top:73px" width="12" height="16"><path d="M6 0a6 6 0 0 0-6 6c0 4.5 6 10 6 10s6-5.5 6-10a6 6 0 0 0-6-6zm0 8.5A2.5 2.5 0 1 1 6 3.5a2.5 2.5 0 0 1 0 5z" fill="#222"/></svg>
  <p class="abs foot-text" style="left:383px;top:70px">Suite 204 / 615 Harlow<br>Street &nbsp;Melbourne &nbsp;3000</p>
  <svg class="abs" style="left:360px;top:136px" width="14" height="14" viewBox="0 0 24 24"><path d="M6.6 10.8a15 15 0 0 0 6.6 6.6l2.2-2.2c.3-.3.7-.4 1-.2 1.1.4 2.3.6 3.6.6.6 0 1 .4 1 1V20c0 .6-.4 1-1 1A17 17 0 0 1 3 4c0-.6.4-1 1-1h3.5c.6 0 1 .4 1 1 0 1.3.2 2.5.6 3.6.1.3 0 .7-.2 1z" fill="#222"/></svg>
  <p class="abs foot-text" style="left:383px;top:134px">1300 482 907</p>
  <svg class="abs" style="left:360px;top:191px" width="14" height="10"><rect width="14" height="10" fill="#222"/><path d="M0 0l7 5 7-5" stroke="#9b86c2" stroke-width="1.5" fill="none"/></svg>
  <p class="abs foot-text" style="left:390px;top:186px">info@brambleridgefootcare.com</p>
  <div class="abs foot-sep" style="left:650px;top:60px;height:170px"></div>
  <h4 class="abs foot-h" style="left:694px;top:26px">Hours of Operation</h4>
  <p class="abs foot-text" style="left:694px;top:72px">Monday to Friday<br>10:00am to 07:00pm</p>
  <p class="abs foot-text" style="left:694px;top:124px">Saturday<br>10:00am to 05:00pm</p>
  <p class="abs foot-text" style="left:694px;top:176px">Sunday<br>By Appointment Only</p>
  <div class="abs brand" style="left:912px;top:94px;font-size:21px;line-height:24px">
    <span class="brand-dot"></span>
    <span>bramble ridge<br>foot<br>care</span>
  </div>
</footer>

<div class="abs bottom">Copyright © 2016 Northvale Studio.&nbsp; All Right Reserved.</div>
<div class="abs social" style="left:928px"></div>
<div class="abs social" style="left:970px"></div>
<div class="abs social" style="left:1012px"></div>

</body>
</html>
```